Cosmetic jar labels,round and wrap around

Hi just starting a small attempt to sell shear butter, with divert flavor all organic and will old Africa formula, would like a wrap around the bottle and also one for the round lid that would have the fragrances name on it , kind of new at this game

Logo Text

Tavelu Naturals by Helen,from the jewel of the east(Uganda)

```html
<!DOCTYPE html>
<html lang="en">
<head>
<meta charset="utf-8">
<title>Tavelu Naturals – Shea Butter Labels</title>
<link rel="stylesheet" href="https://fonts.googleapis.com/css2?family=Montserrat:wght@500;600;800&family=Mrs+Saint+Delafield&display=swap">
<style>
  :root {
    --backdrop: #cdb68c;
    --gold: #b5821f;
    --gold-soft: #c99a3a;
    --ink: #0d0d0d;
    --paper: #f7f5f6;
    --paper-shade: #efeced;
    --white: #ffffff;
  }
  * { margin: 0; padding: 0; box-sizing: border-box; }
  html, body {
    width: 1200px; height: 1024px; overflow: hidden;
    background: var(--backdrop);
    font-family: "Montserrat", "Helvetica Neue", Arial, sans-serif;
  }
  .canvas { position: relative; width: 1200px; height: 1024px; }

  .header-band { position: absolute; left: 0; top: 0; width: 1200px; }
  .header-band__bar { height: 20px; background: var(--gold); }
  .header-band__dots {
    height: 70px;
    background: linear-gradient(180deg, #7a5a1e 0%, #5c4620 50%, #7a5a1e 100%);
  }

  /* Round lid label */
  .lid-label { position: absolute; left: 50px; top: 400px; width: 320px; height: 320px; }
  .lid-label svg { display: block; }
  .lid-label .brand-big { font-family: "Montserrat", sans-serif; font-weight: 800; fill: var(--gold); }
  .lid-label .signature { font-family: "Mrs Saint Delafield", cursive; fill: var(--gold); }
  .lid-label .product { font-family: "Montserrat", sans-serif; font-weight: 500; fill: var(--white); letter-spacing: 1.5px; }
  .lid-label .origin { font-family: "Montserrat", sans-serif; font-weight: 500; fill: var(--ink); letter-spacing: 2.6px; }

  /* Wrap-around label */
  .wrap-label {
    position: absolute; left: 400px; top: 440px; width: 750px; height: 240px;
    display: flex; flex-direction: column;
  }
  .wrap-label__edge { height: 12px; background: var(--gold); flex: none; }
  .wrap-label__pattern {
    height: 40px; flex: none;
    background: linear-gradient(180deg, #8d6e38 0%, #6d5631 50%, #8d6e38 100%);
  }
  .wrap-label__body {
    position: relative; flex: 1;
    background: linear-gradient(180deg, var(--paper) 0%, var(--paper-shade) 100%);
    display: flex; flex-direction: column; align-items: center;
    padding-top: 14px;
  }
  .product-tab {
    position: absolute; left: 50%; top: 0; transform: translateX(-50%);
    width: 162px; height: 54px; background: var(--ink);
    display: flex; flex-direction: column; align-items: center; justify-content: flex-end;
    padding-bottom: 6px;
  }
  .product-tab__rule { width: 26px; height: 1px; background: var(--gold); margin-bottom: 14px; }
  .product-tab__name {
    color: var(--white); font-weight: 500; font-size: 14px; letter-spacing: 1.6px;
  }
  .brand-name { text-align: center; color: var(--gold); font-weight: 800; line-height: 1; }
  .brand-name__first { display: block; font-size: 40px; letter-spacing: 4px; }
  .brand-name__second { display: block; font-size: 23px; letter-spacing: 3px; margin-top: 3px; }
  .signature-line {
    font-family: "Mrs Saint Delafield", cursive; color: var(--gold);
    font-size: 50px; line-height: 1; margin-top: 2px;
  }
  .signature-line small { font-size: 22px; margin-right: 6px; }
  .origin-line {
    font-size: 8.5px; font-weight: 600; letter-spacing: 5.2px; color: var(--ink);
    margin-top: 2px;
  }
</style>
</head>
<body>
<main class="canvas">
  <header class="header-band">
    <div class="header-band__bar"></div>
    <div class="header-band__dots" role="img" aria-label="Dotted gold and black decorative pattern band"></div>
  </header>

  <section class="lid-label" aria-label="Round lid label">
    <svg width="320" height="320" viewBox="0 0 320 320">
      <defs>
        <path id="origin-arc" d="M42 160 A118 118 0 0 0 278 160"/>
      </defs>
      <circle cx="160" cy="160" r="160" fill="var(--gold)"/>
      <circle cx="160" cy="160" r="140" fill="var(--paper)"/>
      <circle cx="160" cy="160" r="134" fill="none" stroke="var(--gold-soft)" stroke-width="2.5"/>
      <text class="brand-big" x="160" y="98" text-anchor="middle" font-size="30" letter-spacing="3">TAVELU</text>
      <text class="brand-big" x="160" y="120" text-anchor="middle" font-size="18" letter-spacing="2">NATURALS</text>
      <text class="signature" x="160" y="165" text-anchor="middle" font-size="38"><tspan font-size="16">by </tspan>Helen</text>
      <path d="M59 182 L261 182 A105 105 0 0 1 59 182 Z" fill="var(--ink)"/>
      <text class="product" x="160" y="208" text-anchor="middle" font-size="12">SHEAR</text>
      <text class="product" x="160" y="225" text-anchor="middle" font-size="12">BUTTER</text>
      <line x1="147" y1="239" x2="173" y2="239" stroke="var(--gold)" stroke-width="1"/>
      <text class="origin" font-size="8.5">
        <textPath href="#origin-arc" startOffset="50%" text-anchor="middle">FROM THE JEWEL OF THE EAST -UGANDA-</textPath>
      </text>
    </svg>
  </section>

  <section class="wrap-label" aria-label="Wrap-around jar label">
    <div class="wrap-label__edge"></div>
    <div class="wrap-label__pattern" role="img" aria-label="Dotted gold and black decorative pattern strip"></div>
    <div class="wrap-label__body">
      <div class="product-tab" style="top:-40px;">
        <span class="product-tab__rule"></span>
        <span class="product-tab__name">SHEAR BUTTER</span>
      </div>
      <h1 class="brand-name" style="margin-top:14px;">
        <span class="brand-name__first">TAVELU</span>
        <span class="brand-name__second">NATURALS</span>
      </h1>
      <p class="signature-line"><small>by</small>Helen</p>
      <p class="origin-line">FROM THE JEWEL OF THE EAST -UGANDA-</p>
    </div>
    <div class="wrap-label__edge"></div>
  </section>
</main>
</body>
</html>
```